Looking for an Innovative Print Design (Service Directory)

We need a new design for our advertisement within a printed colour services directory.

We are a compensation law firm called Velbrook Compensation Lawyers. Feel free to take a browse of our website www.velbrooklegal.com.au to get an idea of what we do and the kind of firm we are.

We are in the process of redeveloping our website and as such, so please don't adhere to the design principles of the current site- impress us with your originality!

On top of any editable formats, your final submissions must include a .pdf copy.
The same design will need to be presented in two dimensions:

- 154mm x 118mm (B1/B2 Half Page);
- 175mm x 113mm (B4 Half Page).

[For more information refer to attached Pdf.]

We have attached for you a few examples of other firms' designs (Sample1,2,3). These are by no means good, or what we're after, it's just to provide you with an idea of what sort of advertisements go into the service directory.

Hi all,

We want to emphasise that a priority of the design is that it must look:
• Professional
• Sophisticated
Please do not hesitate to use completely different colour schemes to the ones that are on our website- as we have said, our website will change in the near future, so cohesion between the current project and the website is not necessary!

Thanks!

Thank you for your submissions so far. There are some great ideas hidden in there. 

An issue we are having is that most of you are conforming to the same understanding of what it should look like. Remember that there is NO NEED to be bound by the image of firm as is. That is, feel free to use a different colour logo.

For inspiration, we relate well to the design aesthetics of: http://www.tinfernstudio.co.uk/

Look forward to seeing your 'out of the box' submissions. 

Reason: We've received a large amount of fantastic designs. However, what we're really looking for is something original. Please feel free to think outside the box (the final design doesn't need to look like a print ad), and construct a design that is completely incongruous with our website! While we do appreciate a minimalistic design, we have yet to receive something that really grabs your attention with its visuals. We're not sure but this may or may not be achieved with a full colour design. Thanks for all your submissions- they all have some features that really click with us. We look forward to the next wave of submissions!

Target Market(s)

We have various target markets, including mainly families, elderly people, blue collar workers.

These are individuals who are looking for assistance. They feel helpless or wronged.

Keep in mind that the people accessing these are those who prefer going to a printed directory rather than using a google search.

Industry/Entity Type

Law Firm

Font styles to use
Serif
Sans Serif

Requirements
Must have
• - Our name 'Velbrook Compensation Lawyers'
- Our logo (attached as logo.eps, logo.png, and logo.tif)
- Must include phone number as 1300 XXX XXX (this must be prominent)
- Must include the following service areas in these words: Motor vehicle claims, medical claims, superannuation claims, Workplace claims, negligence claims
- Our email address: info@velbrooklegal.com.au
- Our website address: www.velbrooklegal.com.au
- The following catchphrases: '98% success rate', and 'No win no fee' in those words
- Our location '412 Carvel Lane, Smithville, SYDNEY'
- For sizing dimensions, we need one in 154mm x 118mm and also a design in 175mm x 113mm (B4 Half Page) [refer to pdf attached]
Nice to have
• - Text indicating free initial consulatation
- Professional colour scheme
- As our website will be changed, do not worry about making the advertisement cohesive with our website design
- We want the design to be modern, but still professional
- Clean typeface
- No gradient colour scheme
- When designing, if you are looking to place more text onto the advertisement, these may be some considerations (feel free to change the wording): Accredited specialists, home and hospital visits

```html
<!DOCTYPE html>
<html lang="en">
<head>
<meta charset="utf-8">
<title>Velbrook Compensation Lawyers – Directory Advertisement</title>
<link href="https://fonts.googleapis.com/css2?family=Lato:wght@300;400&family=Open+Sans:wght@400;600;700&display=swap" rel="stylesheet">
<style>
  :root {
    --page-bg: #e3e3e3;
    --ad-black: #1f1d22;
    --ad-yellow: #f8d200;
    --divider-white: #ffffff;
    --ink: #161616;
    --khaki: #b4a878;
    --caption-grey: #9b9b9b;
  }
  * { box-sizing: border-box; margin: 0; padding: 0; }
  html, body { width: 1200px; height: 1000px; overflow: hidden; }
  body {
    position: relative;
    background: var(--page-bg);
    font-family: "Open Sans", Arial, sans-serif;
  }
  .advert {
    position: absolute;
    left: 43px; top: 28px;
    width: 1102px; height: 844px;
    background: var(--ad-black);
    box-shadow: 6px 8px 10px rgba(0,0,0,0.35);
    overflow: hidden;
  }
  .advert__shapes { position: absolute; inset: 0; }
  .brand {
    position: absolute; left: 63px; top: 44px;
    display: flex; align-items: center; gap: 34px;
    color: var(--ink); font-family: "Lato", sans-serif; font-weight: 400;
  }
  .brand__mark {
    width: 116px; height: 116px; border-radius: 50%;
    background: var(--ink);
  }
  .brand__name { font-size: 64px; letter-spacing: 3px; line-height: 1; }
  .brand__tagline { font-size: 19px; letter-spacing: 3.2px; margin-top: 10px; }
  .services {
    position: absolute; left: 0; top: 210px; width: 645px;
    list-style: none; text-align: center;
    font-family: "Lato", sans-serif; font-weight: 300;
    font-size: 35px; color: var(--ink);
  }
  .services li { height: 73.5px; line-height: 73.5px; }
  .selling-points {
    position: absolute; left: 760px; top: 52px; width: 330px;
    list-style: none; color: var(--khaki);
    font-size: 29px; line-height: 48px; text-transform: uppercase;
  }
  .selling-points li { padding-left: 18px; text-indent: -18px; margin-bottom: 53px; }
  .selling-points li::before { content: "•"; display: inline-block; width: 18px; text-indent: 0; font-size: 20px; }
  .contact {
    position: absolute; left: 0; top: 635px; width: 100%;
    text-align: center; color: #fff;
  }
  .contact__phone {
    color: var(--ad-yellow); font-weight: 700; font-size: 70px;
    letter-spacing: 1px; line-height: 1;
  }
  .contact__lines { font-size: 30px; line-height: 43px; margin-top: 38px; letter-spacing: 0.3px; }
  .size-caption {
    position: absolute; left: 0; top: 900px; width: 100%;
    text-align: center; color: var(--caption-grey);
    font-size: 40px; font-weight: 400;
  }
</style>
</head>
<body>
  <section class="advert">
    <svg class="advert__shapes" viewBox="0 0 1102 844" width="1102" height="844" aria-hidden="true">
      <path fill="var(--ad-yellow)" d="M0,0 H692 C712,100 722,260 700,380 C682,470 655,530 617,568 C470,590 380,602 290,600 C190,597 80,577 0,562 Z"/>
      <path fill="none" stroke="var(--divider-white)" stroke-width="5" d="M692,0 C712,100 722,260 700,380 C682,470 655,530 617,568"/>
      <path fill="none" stroke="var(--divider-white)" stroke-width="5" d="M0,562 C80,577 190,597 290,600 C400,603 550,582 700,562 C850,545 1000,560 1102,578"/>
    </svg>

    <div class="brand">
      <span class="brand__mark"></span>
      <div>
        <div class="brand__name">VELBROOK</div>
        <div class="brand__tagline">COMPENSATION LAWYERS</div>
      </div>
    </div>

    <ul class="services">
      <li>Motor vehicle claims</li>
      <li>Medical claims</li>
      <li>Superannuation claims</li>
      <li>Workplace claims</li>
      <li>Negligence claims</li>
    </ul>

    <ul class="selling-points">
      <li>No win no fee</li>
      <li>98% success rate</li>
      <li>Accredited specialists</li>
      <li>Free initial consulatation</li>
    </ul>

    <div class="contact">
      <div class="contact__phone">1300.246.1357</div>
      <div class="contact__lines">
        <p>info@velbrooklegal.com.au • www.velbrooklegal.com.au</p>
        <p>412 Carvel Lane, Smithville, SYDNEY</p>
      </div>
    </div>
  </section>

  <p class="size-caption">AD 154mm x 118mm</p>
</body>
</html>
```